Flyer-Design für Rücken-Massage, Klangtherapie etc.
Sehr kompetent und schnelle Umsetzung, gute Gestaltung, Farblich in Harmonie. Schnelle Änderungen, bin sehr zufrieden. Danke für die super Arbeit.
Zielgruppe
Rücken-Massage, Klangtherapie, Fußreflex-Massage, Quantenheilung
Aufgabenstellung
Text zu den Rubriken können vom Internet entnommen werden.
https://wohlruhe-tonpraxis.ch/

```html
<!DOCTYPE html>
<html lang="de">
<head>
<meta charset="utf-8">
<title>Flyer Wohlruhe Tonpraxis</title>
<link rel="stylesheet" href="https://fonts.googleapis.com/css2?family=Jost:ital,wght@0,300;0,400;0,500;1,300;1,400;1,600;1,700&display=swap">
<style>
:root{
  --bg:#9c9c9c;
  --paper:#ffffff;
  --orange:#e9782b;
  --green:#9cc54f;
  --green-light:#d9eab4;
  --green-pale:#eef5dd;
  --text:#5a5a5a;
  --text-dark:#444;
  --shade:#f1f1f1;
}
*{margin:0;padding:0;box-sizing:border-box}
html,body{width:1200px;height:826px;overflow:hidden;background:var(--bg)}
body{font-family:"Jost",sans-serif;color:var(--text)}
.canvas{position:relative;width:1200px;height:826px}
.sheet{position:absolute;left:17px;width:1161px;height:387px;background:var(--paper);overflow:hidden}
.sheet--outside{top:22px}
.sheet--inside{top:419px}
.sheet>*{position:absolute}
.wave{left:0;top:0;width:1161px;height:60px}
.shade{left:0;top:0;width:1161px;height:387px}
.heading{font-family:"Jost",sans-serif;font-style:italic;font-weight:700;color:var(--orange);font-size:17px;letter-spacing:-.2px;text-transform:uppercase;line-height:1}
.lead{font-style:italic;font-weight:300;font-size:10.4px;line-height:13px;color:var(--text-dark)}
.body{font-weight:300;font-size:6.3px;line-height:10.9px;color:var(--text)}
.body p+p{margin-top:2px}
.justify{text-align:justify}
.subhead{font-style:italic;font-weight:300;font-size:10.4px;color:var(--text-dark)}
.list{list-style:none;font-weight:300;font-size:6.4px;line-height:10.9px}
.list--dot li::before{content:"• ";}
.list--dash li::before{content:"– ";}
.spaced{font-weight:300;font-size:6.4px;letter-spacing:1.1px;line-height:8.7px;color:var(--text)}
.prices{border-collapse:collapse;font-weight:300;font-size:6.6px;letter-spacing:1px;color:var(--text)}
.prices td{padding:0;line-height:8.8px;vertical-align:top}
.prices .gap td{height:9px}
.prices .dur{padding-left:0;width:55px}
.contact{display:flex;align-items:center;gap:4px;font-weight:300;font-size:5px;letter-spacing:.3px;color:var(--text-dark)}
.contact svg{width:8px;height:8px}
.contact span{margin-right:3px}
.brand{display:flex;align-items:center;gap:7px}
.brand-dot{width:26px;height:26px;border-radius:50%;background:var(--green)}
.brand-name{font-weight:400;font-size:16px;line-height:17px;color:var(--green)}
.photo{display:block}
</style>
</head>
<body>
<main class="canvas">

  <!-- Outside sheet -->
  <section class="sheet sheet--outside">
    <svg class="wave" viewBox="0 0 1161 60" preserveAspectRatio="none">
      <path d="M0 0H775V30C700 52 600 58 480 50C360 42 260 30 150 38C90 42 40 50 0 55Z" fill="var(--green-pale)"/>
      <path d="M0 0H775V22C690 42 600 46 480 38C360 30 250 20 150 28C90 32 40 40 0 46Z" fill="var(--green-light)"/>
      <path d="M0 0H775V10C680 26 600 30 470 24C350 18 250 10 140 16C80 20 40 26 0 32Z" fill="#c4de8c"/>
    </svg>

    <h2 class="heading" style="left:28px;top:56px">Quantenheilung</h2>
    <p class="lead" style="left:30px;top:82px;width:325px">Die Quantenheilung ist der Oberbergriff für viele Transformationen-Methoden die eine positive Veränderung über das höhere Bewusstsein auf unseren allgemein Zustand herbeiführen.</p>
    <div class="body justify" style="left:30px;top:124px;width:322px">
      <p>Es ist das Licht, dass in jeder Seele vorhanden ist und eine hohe Transformationskraft besitzt. Dabei wird davon ausgegangen, dass der Körper Geist, Materie und das gesamte Universum von einem allumfassenden Energiefeld umgeben ist. Dieses Energiefeld enthält Photonen Quanten die mit unserer DNS Verbindungen eingehen. Quantenheilung versetzt das Negative Nervensystem spontan und sofort in einen Zustand in dem tiefe heilende Prozesses stattfinden können. Das Nervensystem schaltet während einer Behandlung unmittelbar auf Heilung um, und kann all das reorganisieren was nicht optimal funktioniert.</p>
      <p>Die Veränderung findet auf den folgenden 3 Ebenen statt, dem denken dem Fühlen und der Körperebene. Mit den Jahren, vielen negativen Erfahrungen und Prägungen vom Leben wurde das Denken enger und härter. Dieses Denken steht unseren Herzenswünschen oft im Weg, sagt uns ,dass es eh nicht schaffen werden, wir nicht gut genug sind, und das wir uns selber nicht trauen können.<br>Mit Quantenheilung kann diese Enge gelöst werden und wieder mehr Leichtigkeit ins Denken einkehren. Und genau so ist es in der Quantenheilung, wenn wir jemanden unterstützen, der Kilometer entfernt ist dies Funktioniert auch über die Distanz, ich habe schon viele Erfahrungen gemacht und die Resultate sind bemerkenswert. Auch bei Tieren habe ich sehr positive Erfahrungen gemacht mit Quantenheilung.</p>
    </div>
    <h3 class="subhead" style="left:30px;top:290px">Glaubenssätze und Blockaden lösen</h3>
    <ul class="list list--dot" style="left:39px;top:308px">
      <li>Partnerschaft Probleme</li>
      <li>Geldmangel und Fehlendes Einkommen</li>
      <li>Veränderung der Beruflichen oder Privaten Lebensumständen</li>
      <li>Gesundheitliche Beschwerden</li>
      <li>Übergewicht</li>
      <li>Zielfindung und Erreichung</li>
      <li>Depressionen / Sexualität Probleme / Missbrauch</li>
    </ul>
    <svg class="photo" role="img" aria-label="Farbige Spirale aus Fraktalmustern in Rot, Grün und Blau" style="left:226px;top:273px;width:180px;height:114px" viewBox="0 0 180 114">
      <defs>
        <radialGradient id="spiralTone" cx="0.62" cy="0.6" r="0.7">
          <stop offset="0" stop-color="#f0c44a"/>
          <stop offset="0.3" stop-color="#4bb5c4"/>
          <stop offset="0.6" stop-color="#3aa66a"/>
          <stop offset="1" stop-color="#c9484e"/>
        </radialGradient>
      </defs>
      <path d="M0 88C0 40 30 2 80 0C140-2 180 40 180 95V114H30C10 114 0 105 0 88Z" fill="url(#spiralTone)"/>
    </svg>

    <h2 class="heading" style="left:456px;top:56px">Über mich</h2>
    <p class="spaced" style="left:456px;top:82px;width:255px">Ich bin in Basel aufgewachsen, und später habe Ich meinen Beruf als Vergolderin absolviert. Viele Jahre später hatte ich diverse Schulungen – Kurse besucht die mir die Möglichkeiten gaben neue Erfahrungen zu sammeln und umzusetzen im Bereich, Geistiger Entspannung.</p>

    <h2 class="heading" style="left:456px;top:134px">Machen Sie den ersten Schritt</h2>
    <p class="spaced" style="left:456px;top:157px;width:260px">JETZT IHR TERMIN BUCHEN<br>Rufen Sie mich an: 076 000 48 27<br>Oder senden Sie mir Ihren Terminvorschlag über mein Kontaktformular.</p>

    <h2 class="heading" style="left:459px;top:204px">Preise</h2>
    <table class="prices" style="left:458px;top:229px">
      <tr><td>FUSSREFLEXMASSAGE</td><td></td><td></td></tr>
      <tr><td>Eine effektive Behandlung</td><td class="dur">45 Min.</td><td>CHF &nbsp; 70.00</td></tr>
      <tr class="gap"><td></td><td></td><td></td></tr>
      <tr><td>KLANGSCHALEN-MASSAGE</td><td></td><td></td></tr>
      <tr><td>Schnupper Einführung Klangmassage:&nbsp;</td><td class="dur">30 Min.</td><td>CHF &nbsp; 60.00</td></tr>
      <tr><td>Klangtherapie-Massage:</td><td class="dur">60 Min.</td><td>CHF &nbsp;100.00</td></tr>
      <tr class="gap"><td></td><td></td><td></td></tr>
      <tr><td>RÜCKEN-NACKENMASSAGE</td><td></td><td></td></tr>
      <tr><td>Eine effektive Behandlung</td><td class="dur">45 Min.</td><td>CHF &nbsp; 70.00</td></tr>
      <tr class="gap"><td></td><td></td><td></td></tr>
      <tr><td>QUANTENHEILUNG</td><td></td><td></td></tr>
      <tr><td>Eine effektive Behandlung</td><td class="dur">60 Min.</td><td>CHF &nbsp;100.00</td></tr>
    </table>

    <p class="spaced" style="left:458px;top:355px">PRAXIS Verena Hollmannsried, Lindenweg 12, 4410 Talbach</p>
    <div class="contact" style="left:458px;top:369px">
      <svg viewBox="0 0 8 8"><rect x=".5" y="1.5" width="7" height="5" fill="none" stroke="#555" stroke-width=".8"/><path d="M.5 1.5L4 4.5L7.5 1.5" fill="none" stroke="#555" stroke-width=".8"/></svg><span>info@wohlruhe-tonpraxis.ch</span>
      <svg viewBox="0 0 8 8"><circle cx="4" cy="4" r="3.4" fill="none" stroke="#555" stroke-width=".8"/><path d="M.6 4H7.4M4 .6C2 2.5 2 5.5 4 7.4M4 .6C6 2.5 6 5.5 4 7.4" fill="none" stroke="#555" stroke-width=".6"/></svg><span>wohlruhe-tonpraxis.ch</span>
      <svg viewBox="0 0 8 8"><path d="M1.6.8L3 .6L3.6 2.4L2.7 3.1C3.2 4.2 3.9 4.9 5 5.4L5.7 4.5L7.4 5.1L7.2 6.6C4 7 1 4 1.6.8Z" fill="#555"/></svg><span>076 000 48 27</span>
    </div>

    <svg class="photo" role="img" aria-label="Porträtfoto der Therapeutin vor grünem Gebüsch" style="left:775px;top:0;width:386px;height:320px" viewBox="0 0 386 320" preserveAspectRatio="none">
      <defs>
        <linearGradient id="portraitTone" x1="0" y1="0" x2="1" y2="1">
          <stop offset="0" stop-color="#5c7a3a"/>
          <stop offset="0.55" stop-color="#8aa260"/>
          <stop offset="1" stop-color="#c0674a"/>
        </linearGradient>
      </defs>
      <path d="M0 0H386V300C300 318 200 312 120 298C70 290 30 292 0 300Z" fill="url(#portraitTone)"/>
    </svg>
    <svg class="wave" style="left:775px;top:280px;width:386px;height:50px" viewBox="0 0 386 50" preserveAspectRatio="none">
      <path d="M0 20C60 10 120 14 190 26C260 38 330 34 386 20V50H0Z" fill="#fff" opacity=".6"/>
      <path d="M0 30C80 22 140 28 200 36C270 44 330 40 386 30V50H0Z" fill="#fff"/>
    </svg>

    <div class="brand" style="left:836px;top:332px">
      <span class="brand-dot"></span>
      <span class="brand-name">Wohlruhe Tonpraxis<br>Verena Hollmannsried</span>
    </div>
    <div class="contact" style="left:852px;top:369px">
      <svg viewBox="0 0 8 8"><rect x=".5" y="1.5" width="7" height="5" fill="none" stroke="#555" stroke-width=".8"/><path d="M.5 1.5L4 4.5L7.5 1.5" fill="none" stroke="#555" stroke-width=".8"/></svg><span>info@wohlruhe-tonpraxis.ch</span>
      <svg viewBox="0 0 8 8"><circle cx="4" cy="4" r="3.4" fill="none" stroke="#555" stroke-width=".8"/><path d="M.6 4H7.4M4 .6C2 2.5 2 5.5 4 7.4M4 .6C6 2.5 6 5.5 4 7.4" fill="none" stroke="#555" stroke-width=".6"/></svg><span>wohlruhe-tonpraxis.ch</span>
      <svg viewBox="0 0 8 8"><path d="M1.6.8L3 .6L3.6 2.4L2.7 3.1C3.2 4.2 3.9 4.9 5 5.4L5.7 4.5L7.4 5.1L7.2 6.6C4 7 1 4 1.6.8Z" fill="#555"/></svg><span>076 000 48 27</span>
    </div>
  </section>

  <!-- Inside sheet -->
  <section class="sheet sheet--inside">
    <svg class="shade" viewBox="0 0 1161 387" preserveAspectRatio="none">
      <path d="M0 60L388 170L388 387H0Z" fill="var(--shade)"/>
      <path d="M388 170L775 50L775 387H388Z" fill="#f5f5f5"/>
      <path d="M775 50L1161 150V387H775Z" fill="var(--shade)"/>
      <path d="M0 300L180 250L388 330V387H0Z" fill="#fafafa"/>
    </svg>
    <svg class="wave" viewBox="0 0 1161 60" preserveAspectRatio="none">
      <path d="M0 0H1161V30C1060 48 960 52 860 46C760 40 680 30 560 40C440 50 330 56 220 48C130 42 60 46 0 52Z" fill="var(--green-pale)"/>
      <path d="M0 0H1161V20C1060 38 960 42 860 36C760 30 680 22 560 30C440 38 330 44 220 36C130 30 60 34 0 40Z" fill="var(--green-light)"/>
      <path d="M0 0H1161V8C1060 24 960 28 860 22C760 16 680 10 560 16C440 22 330 26 220 20C130 16 60 20 0 26Z" fill="#c4de8c"/>
    </svg>

    <h2 class="heading" style="left:9px;top:53px">Fussreflexmassage</h2>
    <p class="lead" style="left:66px;top:78px;width:300px">Die Blockaden werden gelöst,<br>ein Wohlbefinden wird sich wieder einstellen,<br>so das die Harmonie und das Gleichgewicht zum fliessen vereint.</p>
    <div class="body justify" style="left:66px;top:121px;width:279px">
      <p>Fussreflexzonenmassage ist eine Methode, mit welcher ich Ihre körpereigenen Heilungskräfte aktivieren werde. Von altertümlichen Texten, Illustrationen und Artefakten weiss man, dass die frühen chinesischen, japanischen, ägyptischen und indianischen Kulturen schon die Behandlung an den Füssen gefördert haben.<br>Das Prinzip von der Fussreflexzonenmassage beruht auf der Erkenntnis, dass Energiezonen durch den Körper laufen. In den Füssen reflektieren sich diese Zonen und korrespondieren mit den wichtigen Organen, Drüsen und anderen Körperteilen.</p>
      <p>Stimuliert oder bearbeitet man nun mit Druck von Finger und Daumen diese Zonen am Fuss, beeinflusst das die entsprechende Zone im ganzen Körper. Der Therapeut stimuliert über 1'000 Nervenenden während einer Fussreflexzonenmassage.</p>
    </div>
    <h3 class="subhead" style="left:32px;top:260px">Wie wirkt sie?</h3>
    <p class="body justify" style="left:32px;top:274px;width:137px">Der Körper wird von Kopf bis Fuss von 10 Energiezonen durchlaufen – 5 auf jeder Seite des Körpers. Alle Organe und Körperteile liegen an einer oder mehrerer dieser Zonen. Jede Zone stellt ein Kanal für die nicht greifbare Lebensenergie dar. In der orientalischen Medizin nennt man es chi oder qi.</p>
    <svg class="photo" role="img" aria-label="Foto einer Fussreflexmassage mit Händen an einer Fusssohle und einer pinken Blüte" style="left:177px;top:231px;width:304px;height:156px" viewBox="0 0 304 156">
      <defs>
        <linearGradient id="footTone" x1="0" y1="0" x2="1" y2="1">
          <stop offset="0" stop-color="#cfe3a6"/>
          <stop offset="0.5" stop-color="#efc3a4"/>
          <stop offset="1" stop-color="#d9e6c0"/>
        </linearGradient>
      </defs>
      <path d="M0 156C0 70 60 0 150 0C240 0 304 70 304 156Z" fill="url(#footTone)"/>
    </svg>

    <h2 class="heading" style="left:406px;top:61px">Rücken-Nackenmassage</h2>
    <p class="lead" style="left:428px;top:88px;width:300px">Durch leichten bis starken Druck<br>werden Muskelverspannungen massiert, gestrichen und geknetet.</p>
    <p class="body justify" style="left:428px;top:117px;width:280px">Nacken-Schulter und Rückenverspannungen können gelöst werden Gelenk-und Muskelschmerzen können dabei gelindert werden. Die Durchblutung wird dabei gefördert, das Hautbild verbessert, die Sauerstoffzufuhr im Blut wird vermehrt, der Stoffwechsel angeregt, der Körper entgiftet und Schlackstoffe werden abtransportiert.</p>
    <h3 class="subhead" style="left:445px;top:174px">Wirkungsweise:</h3>
    <ul class="list list--dash" style="left:445px;top:189px">
      <li>steigert lokale Durchblutung</li>
      <li>entspannt Haut, Bindegewebe<br>&nbsp;&nbsp;&nbsp;und Muskulatur</li>
      <li>löst Verklebungen und Narben</li>
      <li>senkt Blutdruck und Pulsfrequenz</li>
      <li>lindert Schmerzen</li>
      <li>bringt psychische Entspannung</li>
      <li>reduziert Stress</li>
    </ul>
    <svg class="photo" role="img" aria-label="Foto einer Rückenmassage an einer liegenden Person" style="left:560px;top:169px;width:215px;height:218px" viewBox="0 0 215 218">
      <defs>
        <linearGradient id="backTone" x1="0" y1="0" x2="1" y2="1">
          <stop offset="0" stop-color="#3f4a2a"/>
          <stop offset="0.45" stop-color="#b9805a"/>
          <stop offset="1" stop-color="#e8e2da"/>
        </linearGradient>
      </defs>
      <path d="M70 0H215V218H30C10 180 0 140 0 100C0 50 25 10 70 0Z" fill="url(#backTone)"/>
    </svg>

    <h2 class="heading" style="left:812px;top:61px">Klangschalen-Massage</h2>
    <p class="lead" style="left:842px;top:93px;width:310px">Die Blockaden werden gelöst,<br>ein Wohlbefinden wird sich wieder einstellen,<br>so das die Harmonie und das Gleichgewicht zum fliessen vereint.</p>
    <p class="body justify" style="left:842px;top:136px;width:280px">Durch die heilsamen Klänge werde ich Ihnen Ihre tiefsitzende Verspannungen lösen, wodurch die Selbstheilungskräfte Ihres Körpers freigesetzt und mobilisiert werden. Durch die Klangschalenmassage kann sehr schnell ein äusserst tiefer Entspannungszustand beim Behandelten erreicht werden. Die Töne der Klangschalen erinnern die Menschen an etwas ursprüngliches und Vertrautes und vermitteln dadurch ein entspannendes und wohliges Körpergefühl.</p>
    <h3 class="subhead" style="left:806px;top:218px">Wie wirkt sie?</h3>
    <p class="body justify" style="left:806px;top:233px;width:137px">Indem es durch den Einsatz der Klangschalen besser gelingt, dass sich der Körper entkrampft und die Seele sich besser öffnen kann, wirkt auch die Massage dadurch wesentlich intensiver und hat eine langanhaltende positive Wirkung auf Körper und Seele.<br>Indem jede einzelne Körperzelle durch die entspannende Klänge angesprochen wird, fühlt sich der Patient in seiner Gesamtheit wieder wesentlich harmonischer und kann neue Selbstheilungskräfte entwickeln, die auch wieder zu neuer Lebensenergie verhelfen.</p>
    <svg class="photo" role="img" aria-label="Foto goldener Klangschalen mit weisser Orchidee auf rotem Tuch" style="left:955px;top:184px;width:206px;height:203px" viewBox="0 0 206 203" preserveAspectRatio="none">
      <defs>
        <linearGradient id="bowlTone" x1="0" y1="0" x2="1" y2="1">
          <stop offset="0" stop-color="#8a6a3c"/>
          <stop offset="0.5" stop-color="#c99a4e"/>
          <stop offset="1" stop-color="#7a3a22"/>
        </linearGradient>
      </defs>
      <rect width="206" height="203" fill="url(#bowlTone)"/>
    </svg>
  </section>

</main>
</body>
</html>
```